Property Management Company looking for a high-end business card, letterhead and envelope design.

We provide high-end / boutique property management for real estate investors or individuals looking for someone to manage their portfolio. we are looking for a cohesive high-end design for our business cards, letterhead and envelopes.

Target Market(s)

Real Estate Investors

Industry/Entity Type

Real Estate

Requirements
Must have
• business card, letterhead and envelope design - logo attached

```html
<!DOCTYPE html>
<html lang="en">
<head>
<meta charset="utf-8">
<title>Keel Harbor Property Management – Stationery</title>
<link rel="stylesheet" href="https://fonts.googleapis.com/css2?family=Montserrat:wght@500;600&family=PT+Sans:wght@400&display=swap">
<style>
  :root {
    --brand-blue: #2c5a8c;
    --envelope-blue: #2f5f96;
    --envelope-flap: #3566a0;
    --accent-grey: #a9abae;
    --paper: #fbfbfb;
    --ink: #2e3440;
    --backdrop: #e8e9eb;
  }
  html, body {
    margin: 0;
    padding: 0;
    width: 1200px;
    height: 1200px;
    overflow: hidden;
    background: var(--backdrop);
  }
  .stage {
    position: relative;
    width: 1000px;
    height: 1000px;
    transform: scale(1.2);
    transform-origin: 0 0;
  }
  .sheet {
    position: absolute;
    background: var(--paper);
    box-shadow: 0 1px 3px rgba(0,0,0,0.12);
    overflow: hidden;
  }
  .band { position: absolute; }
  .band--blue { background: var(--brand-blue); }
  .band--grey { background: var(--accent-grey); }

  .wordmark {
    position: absolute;
    font-family: "Montserrat", sans-serif;
    color: var(--brand-blue);
    line-height: 1;
    white-space: nowrap;
  }
  .wordmark__name {
    display: block;
    font-weight: 600;
    letter-spacing: 0.06em;
  }
  .wordmark__tagline {
    display: block;
    font-weight: 500;
    letter-spacing: 0.12em;
  }

  /* Letterhead */
  .letterhead { left: 14px; top: 262px; width: 416px; height: 538px; }
  .letterhead .band { top: 11px; height: 20px; }
  .letterhead .band--blue { left: 0; width: 328px; }
  .letterhead .band--grey { left: 351px; width: 65px; }
  .letterhead .wordmark { left: 57px; top: 70px; }
  .letterhead .wordmark__name { font-size: 21px; }
  .letterhead .wordmark__tagline { font-size: 9.6px; margin-top: 5px; }
  .letter-body {
    position: absolute;
    left: 54px;
    top: 186px;
    width: 305px;
    font-family: "PT Sans", sans-serif;
    font-size: 8.6px;
    line-height: 11.2px;
    color: var(--ink);
  }
  .letter-body p { margin: 0 0 11px; }

  /* Business card – contact side */
  .card-contact { left: 572px; top: 266px; width: 173px; height: 100px; }
  .card-contact .band--grey { left: 0; top: 0; width: 64px; height: 7px; }
  .card-contact .band--blue.top { left: 75px; top: 0; width: 98px; height: 7px; }
  .contact-panel {
    position: absolute;
    left: 75px; top: 17px; width: 98px; height: 83px;
    background: var(--brand-blue);
  }
  .card-contact .wordmark { left: 7px; top: 46px; }
  .card-contact .wordmark__name { font-size: 8.2px; }
  .card-contact .wordmark__tagline { font-size: 3.9px; margin-top: 1.5px; }
  .contact-list {
    list-style: none;
    margin: 0;
    padding: 0;
    position: absolute;
    left: 6px; top: 10px;
    font-family: "Montserrat", sans-serif;
    font-size: 4px;
    letter-spacing: 0.08em;
    color: #fff;
  }
  .contact-list li {
    display: flex;
    align-items: flex-start;
    gap: 7px;
    height: 13px;
  }
  .contact-list svg { width: 6px; height: 6px; flex: none; fill: #fff; }
  .contact-list span { padding-top: 1px; line-height: 5px; }

  /* Business card – logo side */
  .card-logo { left: 785px; top: 268px; width: 173px; height: 100px; }
  .card-logo .wordmark { left: 0; right: 0; top: 43px; text-align: center; }
  .card-logo .wordmark__name { font-size: 11.5px; }
  .card-logo .wordmark__tagline { font-size: 5.4px; margin-top: 2px; }
  .card-logo .band--blue { left: 0; top: 80px; width: 173px; height: 12px; }

  /* Envelope – front */
  .envelope-front { left: 573px; top: 418px; width: 415px; height: 172px; }
  .envelope-note {
    position: absolute;
    left: 58px; top: 66px; width: 166px;
    font-family: "PT Sans", sans-serif;
    font-size: 5px;
    line-height: 7.2px;
    text-align: right;
    color: var(--ink);
    margin: 0;
  }
  .envelope-front .wordmark { left: 243px; top: 76px; }
  .envelope-front .wordmark__name { font-size: 13.5px; }
  .envelope-front .wordmark__tagline { font-size: 6.6px; margin-top: 2px; }
  .return-address {
    position: absolute;
    left: 239px; top: 142px;
    font-family: "PT Sans", sans-serif;
    font-size: 4.4px;
    line-height: 6px;
    color: var(--ink);
    margin: 0;
  }

  /* Envelope – back */
  .envelope-back {
    position: absolute;
    left: 570px; top: 617px; width: 425px; height: 180px;
    box-shadow: 0 1px 3px rgba(0,0,0,0.15);
  }
  .envelope-back svg { display: block; }
</style>
</head>
<body>
<main class="stage">

  <section class="sheet letterhead" aria-label="Letterhead">
    <div class="band band--blue"></div>
    <div class="band band--grey"></div>
    <div class="wordmark">
      <span class="wordmark__name">KEEL HARBOR</span>
      <span class="wordmark__tagline">PROPERTY MANAGEMENT</span>
    </div>
    <div class="letter-body">
      <p>Lorem ipsum dolor sit amet, consectetuer adipiscing elit, sed diam nonummy nibh euismod tincidunt ut laoreet dolore magna aliquam erat volutpat. Ut wisi enim ad minim veniam, quis nostrud exerci tation ullamcorper suscipit lobortis nisl ut aliquip ex ea commodo consequat. Duis autem vel eum iriure dolor in hendrerit in vulputate velit esse molestie consequat, vel illum dolore eu feugiat nulla facilisis at vero eros et accumsan et iusto odio dignissim qui blandit praesent luptatum zzril delenit augue duis dolore te feugait nulla facilisi.</p>
      <p>Lorem ipsum dolor sit amet, consectetuer adipiscing elit, sed diam nonummy nibh euismod tincidunt ut laoreet dolore magna aliquam erat volutpat. Ut wisi enim ad minim veniam, quis nostrud exerci tation ullamcorper suscipit lobortis nisl ut aliquip ex ea commodo consequat. Duis autem vel eum iriure dolor in hendrerit in vulputate velit esse molestie consequat, vel illum dolore eu feugiat nulla facilisis at vero eros et accumsan et iusto odio dignissim qui blandit praesent luptatum zzril delenit augue duis dolore te feugait nulla facilisi.</p>
      <p>Lorem ipsum dolor sit amet, consectetuer adipiscing elit, sed diam nonummy nibh euismod tincidunt ut laoreet dolore magna aliquam erat volutpat. Ut wisi enim ad minim veniam, quis nostrud exerci tation ullamcorper suscipit lobortis nisl ut aliquip ex ea commodo consequat. Duis autem vel eum iriure dolor in hendrerit in vulputate velit esse molestie consequat, vel illum dolore eu feugiat nulla facilisis at vero eros et accumsan et iusto odio dignissim qui blandit praesent luptatum zzril delenit augue duis dolore te feugait nulla facilisi.</p>
    </div>
  </section>

  <section class="sheet card-contact" aria-label="Business card, contact side">
    <div class="band band--grey"></div>
    <div class="band band--blue top"></div>
    <div class="wordmark">
      <span class="wordmark__name">KEEL HARBOR</span>
      <span class="wordmark__tagline">PROPERTY MANAGEMENT</span>
    </div>
    <div class="contact-panel">
      <ul class="contact-list">
        <li>
          <svg viewBox="0 0 24 24" aria-hidden="true"><path d="M6.6 10.8a15 15 0 0 0 6.6 6.6l2.2-2.2a1 1 0 0 1 1-.25 11.4 11.4 0 0 0 3.6.57 1 1 0 0 1 1 1V20a1 1 0 0 1-1 1A17 17 0 0 1 3 4a1 1 0 0 1 1-1h3.5a1 1 0 0 1 1 1c0 1.25.2 2.45.57 3.57a1 1 0 0 1-.25 1z"/></svg>
          <span>+00 (000) 555 0142</span>
        </li>
        <li>
          <svg viewBox="0 0 24 24" aria-hidden="true"><path d="M2 5h20v14H2z M4 7v.5l8 5 8-5V7z" fill-rule="evenodd"/></svg>
          <span>INFO@KEELHARBOR.COM</span>
        </li>
        <li>
          <svg viewBox="0 0 24 24" aria-hidden="true"><path d="M12 2a10 10 0 1 0 0 20 10 10 0 0 0 0-20zm0 2c.9 0 2.2 2.3 2.6 7H9.4C9.8 6.3 11.1 4 12 4zM4.1 13h3.3c.1 2.2.5 4.1 1.1 5.5A8 8 0 0 1 4.1 13zm0-2a8 8 0 0 1 4.4-5.5c-.6 1.4-1 3.3-1.1 5.5zm7.9 9c-.9 0-2.2-2.3-2.6-7h5.2c-.4 4.7-1.7 7-2.6 7zm3.5-1.5c.6-1.4 1-3.3 1.1-5.5h3.3a8 8 0 0 1-4.4 5.5zm1.1-7.5c-.1-2.2-.5-4.1-1.1-5.5a8 8 0 0 1 4.4 5.5z"/></svg>
          <span>WWW.KEELHARBOR.COM</span>
        </li>
        <li>
          <svg viewBox="0 0 24 24" aria-hidden="true"><path d="M12 2a7 7 0 0 0-7 7c0 5.2 7 13 7 13s7-7.8 7-13a7 7 0 0 0-7-7zm0 9.5A2.5 2.5 0 1 1 12 6.5a2.5 2.5 0 0 1 0 5z"/></svg>
          <span>120 HARBOR LANE<br>SUITE 4, PORTLAND<br>POSTAL 00000</span>
        </li>
      </ul>
    </div>
  </section>

  <section class="sheet card-logo" aria-label="Business card, logo side">
    <div class="wordmark">
      <span class="wordmark__name">KEEL HARBOR</span>
      <span class="wordmark__tagline">PROPERTY MANAGEMENT</span>
    </div>
    <div class="band band--blue"></div>
  </section>

  <section class="sheet envelope-front" aria-label="Envelope, front">
    <p class="envelope-note">Lorem ipsum dolor sit amet, consectetuer adipiscing elit. Cras at tempus dui. Aliquam urna tortor, convallis in justo eu, tempor porttitor nunc. Aliquam lacinia nisi malesuada, blandit ligula facilisis, iaculis dolor. Cras vehicula massa. Etiam posuere convallis dignissim. Etiam at quam ornare, mattis eros ut, blandit mi. Ut sit amet sapien eget odio eleifend hendrerit sed eu velit. Fusce eu lacus ac erat facilisis sit amet.</p>
    <div class="wordmark">
      <span class="wordmark__name">KEEL HARBOR</span>
      <span class="wordmark__tagline">PROPERTY MANAGEMENT</span>
    </div>
    <p class="return-address">120 Harbor Lane, Suite 4<br>Portland, Postal 00000</p>
  </section>

  <section class="envelope-back" aria-label="Envelope, back">
    <svg width="425" height="180" viewBox="0 0 425 180">
      <rect class="envelope-body" width="425" height="180" fill="var(--envelope-blue)"/>
      <path class="envelope-flap" d="M0 0 L425 0 L425 8 L232 66 Q212 72 193 66 L0 8 Z" fill="var(--envelope-flap)"/>
      <path d="M0 8 L193 66 Q212 72 232 66 L425 8" fill="none" stroke="rgba(0,0,0,0.18)" stroke-width="1"/>
    </svg>
  </section>

</main>
</body>
</html>
```